Occupational Therapy promotional poster

We need 2 x A4 posters to be created:
- 1 with a male super hero
- 1 with a female super hero (see suggested design).

These posters will be used for a promotional campaign celebrating occupational therapy. The idea being that occupational therapists are our local superhero. We see them as the ‘unsung heroes’ of our local communities, so this campaign is a play on that idea.

These posters will be displayed on community notice boards and in hospitals. They will also be used on display tables promoting what occupational therapy is. They will also potentially be used as handouts in presentations. We plan to use these posters for the coming 2 years.

As these will be displayed on noticeboards they need to be bright and colourful. The colours suggested in the attachment are the types of colours we would like used (blue, yellow and red).

We envision these posters being displayed side by side.

Although we are open to interpretation of the “super hero” theme – we particularly liked the black super hero images as they look similar to the symbol for wheelchair access (which occupational therapists use).

Alternatively, a comic book inspired design would also be appealing – see inspiration images in attached document.

See the images that we have drawn inspiration from. I've included the black generic super heroes as well as the comic book style.

This design needs to include the KLRV-PTB logo which is included.

The superhero also needs to have a starwarden style logo somewhere visable. This could be on their chest or on their cape – depending on their angle. Instead of the Starwarden ‘S’, please put ‘OT’.

The content for both posters is identical. However, we would like 1 male version of the poster and 1 female version of the poster.

The superhero graphic needs to be G-rated. For the female graphic - it cannot include cleavage or clothing that is too tight/revealing.

Based on the locations where the poster will be displayed, it does need to have a professional feel.

ATTACHED:
- the KLRV-PTB Logo (to be included)
- a design brief + all text that needs to be included
- an example of the type of posters that we are envisioning

Target Market(s)

General public in New Zealand: Patients in hospital waiting rooms, mothers of children in childcare, elderly people who look at notice boards

Industry/Entity Type

Health Care

Font styles to use
Sans Serif

Requirements
Must have
• 2 A4 twin posters. Identical content but 1 female version and 1 male version
• The KLRV-PTB logo (attached)
• A "superhero" symbol on the chest or cape of the superhero. It should look like the starwarden symbol but instead say "OT" rather than S.
• Must be bright and colourful
• Must include all text included
Should not have
• Any nudity, revealing poses or tight clothing. G-rated.

```html
<!DOCTYPE html>
<html lang="en">
<head>
<meta charset="utf-8">
<title>Meet Your Local Superhero – The Occupational Therapist</title>
<link rel="stylesheet" href="https://fonts.googleapis.com/css2?family=Barlow+Condensed:ital,wght@0,600;1,700;1,800;1,900&family=Open+Sans:wght@400;700&family=Roboto+Slab:wght@500;700&display=swap">
<style>
  :root {
    --purple: #4e1a5e;
    --purple-dark: #3a1247;
    --yellow: #ffd21f;
    --gold: #f6a81c;
    --cream: #fff6c9;
    --ink: #8a2a12;
    --white: #ffffff;
    --hero-red: #c8262a;
    --profile-bg: rgba(60, 22, 70, 0.82);
  }
  * { box-sizing: border-box; margin: 0; padding: 0; }
  html, body { width: 851px; height: 1200px; overflow: hidden; }
  body { background: var(--purple); font-family: "Open Sans", sans-serif; }

  .poster {
    position: relative;
    width: 851px;
    height: 1200px;
    overflow: hidden;
    background:
      radial-gradient(ellipse 70% 60% at 62% 58%, #fff3a6 0%, var(--yellow) 30%, var(--gold) 62%, var(--purple) 100%);
  }
  .poster__top {
    position: absolute; left: 0; top: 0; width: 100%; height: 210px;
    background: linear-gradient(180deg, var(--purple-dark) 0%, var(--purple) 80%, rgba(78,26,94,0) 100%);
  }

  .title { position: absolute; left: 0; top: 0; width: 100%; height: 205px; }
  .title__kicker {
    position: absolute; right: 28px; top: 32px;
    font-family: "Barlow Condensed", sans-serif; font-style: italic; font-weight: 800;
    font-size: 54px; line-height: 1; color: var(--white); letter-spacing: 1px;
  }
  .title__main {
    position: absolute; right: 24px; top: 78px;
    font-family: "Barlow Condensed", sans-serif; font-style: italic; font-weight: 900;
    font-size: 104px; line-height: 1; color: var(--yellow); letter-spacing: 2px;
    text-shadow: 3px 3px 0 var(--purple-dark);
  }
  .title__sub {
    position: absolute; left: 84px; top: 166px;
    font-family: "Barlow Condensed", sans-serif; font-weight: 600;
    font-size: 34px; line-height: 1; color: var(--cream); letter-spacing: 2px;
  }

  .intro {
    position: absolute; left: 22px; top: 212px; width: 808px;
    padding: 12px 16px 14px;
    background: linear-gradient(180deg, rgba(255,246,201,0.95), rgba(255,240,170,0.75));
    color: var(--ink); font-size: 13.4px; line-height: 1.42;
  }
  .intro p { margin-bottom: 12px; }
  .intro h2 {
    font-size: 13.4px; font-weight: 700; color: var(--purple); text-transform: uppercase;
    margin-bottom: 2px;
  }
  .intro p:last-child { margin-bottom: 0; }

  .hero-figure {
    position: absolute; left: 478px; top: 470px; width: 250px; height: 550px;
    border-radius: 110px 110px 30px 30px;
    background: linear-gradient(160deg, #2a1630 0%, #3a1c44 45%, var(--hero-red) 100%);
    opacity: 0.92;
  }

  .profile {
    position: absolute; left: 26px; top: 548px; width: 436px; height: 470px;
    padding: 18px 22px;
    background: var(--profile-bg);
    color: var(--white); font-size: 13.2px; line-height: 1.5;
  }
  .profile h2 {
    font-family: "Barlow Condensed", sans-serif; font-weight: 600;
    font-size: 21px; letter-spacing: 1px; color: var(--yellow); margin-bottom: 10px;
  }
  .profile__lead { margin-bottom: 4px; }
  .profile ul { list-style: none; }
  .profile li { position: relative; padding-left: 12px; margin-bottom: 4px; }
  .profile li::before { content: "•"; position: absolute; left: 0; }

  .footer {
    position: absolute; left: 0; top: 1035px; width: 100%; height: 165px;
    background: var(--purple);
  }
  .footer__cta {
    position: absolute; left: 30px; top: 34px; width: 580px;
    font-family: "Roboto Slab", serif; font-weight: 500;
    font-size: 22px; line-height: 1.3; color: var(--yellow);
  }
  .brand {
    position: absolute; right: 22px; top: 22px; width: 190px; height: 126px;
    background: var(--white);
    display: flex; align-items: center; justify-content: center; gap: 10px;
    padding: 8px;
  }
  .brand__dot { width: 22px; height: 22px; border-radius: 50%; background: var(--purple); }
  .brand__name {
    font-family: "Open Sans", sans-serif; font-weight: 700; font-size: 20px;
    color: var(--purple); line-height: 1;
  }
</style>
</head>
<body>
<main class="poster">
  <div class="poster__top"></div>

  <header class="title">
    <div class="title__kicker">MEET YOUR LOCAL</div>
    <h1 class="title__main">SUPERHERO</h1>
    <div class="title__sub">THE OCCUPATIONAL THERAPIST</div>
  </header>

  <section class="intro">
    <p>Imagine being defeated by an everyday task like putting your clothes on, catching a bus, spending time with your friends or taking care of yourself.</p>
    <h2>Occupational therapy is here to help.</h2>
    <p>The things that you do – your occupations – help express who you are, how you feel about yourself, and how you connect with others. Your health and wellbeing will be affected if you are unable to do the things you want and need to do, to live and enjoy your life.</p>
    <h2>Occupational therapists help people of all ages and work in a variety of settings.</h2>
    <p>Occupations that could cause difficulty include preparing and eating meals, driving and mobility; recreation and exercise; use of a computer or workstation; showering or bathing; getting things done on time and in a preferred standard, having enough things to do and the confidence to do them; developing supportive relationships or friendships; or thriving in school.</p>
  </section>

  <div class="hero-figure" role="img" aria-label="Illustration of a superhero in a dark suit and red cape with an OT emblem, standing hands on hips"></div>

  <section class="profile">
    <h2>SUPERHERO PROFILE</h2>
    <p class="profile__lead">My super powers help people to:</p>
    <ul>
      <li>Learn new ways of doing things following an illness or injury (e.g. dressing or cooking)</li>
      <li>Thrive in their senior years</li>
      <li>Regulate their strong emotions</li>
      <li>Achieve their goals at school</li>
      <li>Develop ways to manage pain</li>
      <li>Develop their confidence in social situations</li>
      <li>Access support available in the community</li>
      <li>Adapt material or equipment (e.g. wheelchairs or provide a special bath or toilet seat)</li>
      <li>Make changes to their living or working environment</li>
      <li>Develop new skills, abilities or interests (e.g. job readiness programmes)</li>
    </ul>
  </section>

  <footer class="footer">
    <p class="footer__cta">JOIN US in celebrating occupational therapy<br>by using the hashtag #HeroNextDoorNZ<br>Visit klrv.co.nz for more information</p>
    <div class="brand">
      <span class="brand__dot"></span>
      <span class="brand__name">KLRV-PTB</span>
    </div>
  </footer>
</main>
</body>
</html>
```